Post Lockdown Ortho Special

We are running a special for (Ortho) Braces/Clear Aligner (Quorvelina), till July 31st 2020. Up to $2,000 off with free Consultation and Xrays.

We need a ad to run in different formats.

Maybe something with: what better time to get braces when you have to wear a mask all the time.

Trying to rebuild our business and get people in for free consultations.

```html
<!DOCTYPE html>
<html lang="en">
<head>
<meta charset="utf-8">
<title>Ridgeline Family Dentistry – Ortho Special Offer</title>
<link rel="stylesheet" href="https://fonts.googleapis.com/css2?family=Montserrat:wght@300;400;500;600;700;800&family=Great+Vibes&display=swap">
<style>
  :root {
    --purple: #6a419b;
    --purple-deep: #5b3389;
    --gold: #e8c65a;
    --gold-dark: #c9a437;
    --ink: #231f20;
    --white: #ffffff;
    --stage: #dcdcdc;
    --font-sans: "Montserrat", Arial, sans-serif;
    --font-script: "Great Vibes", cursive;
  }
  html, body {
    margin: 0;
    padding: 0;
    width: 1200px;
    height: 1061px;
    overflow: hidden;
    background: var(--stage);
  }
  .flyer {
    position: absolute;
    left: 0;
    top: 65px;
    width: 1200px;
    height: 931px;
    display: block;
  }
  .sans { font-family: var(--font-sans); }
  .script { font-family: var(--font-script); }
  .brand-text { font-family: var(--font-sans); font-weight: 600; fill: var(--purple); }
  .intro { font-family: var(--font-sans); font-weight: 500; font-size: 27px; fill: var(--white); }
  .offer-script { font-family: var(--font-script); font-size: 190px; fill: var(--gold); }
  .offer-word { font-family: var(--font-sans); font-weight: 300; font-size: 150px; fill: var(--gold); }
  .treatment { font-family: var(--font-sans); font-weight: 500; font-size: 26px; fill: var(--white); }
  .badge-lead { font-family: var(--font-sans); font-weight: 700; font-size: 38px; fill: var(--purple); }
  .badge-amount { font-family: var(--font-sans); font-weight: 800; font-size: 42px; fill: var(--ink); }
  .badge-note { font-family: var(--font-sans); font-weight: 500; font-size: 20px; fill: var(--purple); }
  .badge-date { font-family: var(--font-sans); font-weight: 700; font-size: 20px; fill: var(--purple); }
  .badge-date .dark { fill: var(--ink); }
  .headline { font-family: var(--font-sans); font-weight: 800; font-size: 33px; fill: var(--purple); }
  .headline .dark { fill: var(--ink); }
  .cta { font-family: var(--font-sans); font-weight: 500; font-size: 28px; fill: var(--white); }
  .cta .strong { font-weight: 800; }
  .phone { font-family: var(--font-sans); font-weight: 800; font-size: 58px; fill: var(--gold); }
  .email { font-family: var(--font-sans); font-weight: 400; font-size: 27px; fill: var(--white); }
</style>
</head>
<body>
<svg class="flyer" viewBox="0 0 1287 998" xmlns="http://www.w3.org/2000/svg" aria-label="Ortho special offer flyer">
  <defs>
    <linearGradient id="goldSweep" x1="0" y1="0" x2="1" y2="0">
      <stop offset="0" stop-color="#d9b545"/>
      <stop offset="0.45" stop-color="#f3da86"/>
      <stop offset="1" stop-color="#d4ad3c"/>
    </linearGradient>
    <linearGradient id="photoTone" x1="0" y1="0" x2="1" y2="1">
      <stop offset="0" stop-color="#f1ece8"/>
      <stop offset="0.45" stop-color="#e9d3c2"/>
      <stop offset="0.75" stop-color="#d9b68f"/>
      <stop offset="1" stop-color="#efe7e1"/>
    </linearGradient>
  </defs>

  <!-- Base -->
  <rect class="paper" x="0" y="0" width="1287" height="998" fill="var(--white)"/>

  <!-- Purple offer panel -->
  <path class="offer-panel" d="M0 215 C 220 178 470 172 700 198 L 840 800 C 560 810 230 760 0 672 Z" fill="var(--purple)"/>

  <!-- Family photograph area -->
  <path class="family-photo" role="img" aria-label="Photo of a smiling family of four lying head to head on white bedding"
        d="M722 0 H1287 V690 C 1150 745 1000 775 860 785 C 760 620 600 330 722 0 Z" fill="url(#photoTone)"/>

  <!-- Thin gold edge along the photo -->
  <path class="photo-edge" d="M722 0 C 615 220 630 430 770 570 C 830 640 860 710 875 785" fill="none" stroke="url(#goldSweep)" stroke-width="6"/>

  <!-- Contact band -->
  <path class="contact-band" d="M680 998 L 688 828 C 900 812 1110 762 1287 668 V 998 Z" fill="var(--ink)"/>

  <!-- Gold sweep -->
  <path class="gold-sweep" d="M40 655 C 150 760 450 798 760 790 C 1000 782 1150 742 1262 660 C 1160 770 960 822 760 828 C 450 834 150 782 40 655 Z" fill="url(#goldSweep)"/>

  <!-- Brand name -->
  <g class="brand">
    <text class="brand-text" x="243" y="113" font-size="50" letter-spacing="1">RIDGELINE</text>
    <text class="brand-text" x="243" y="134" font-size="16" letter-spacing="7.6">FAMILY DENTISTRY</text>
    <line x1="243" y1="142" x2="538" y2="142" stroke="var(--purple)" stroke-width="1.2" opacity="0.6"/>
    <text class="brand-text" x="390" y="164" font-size="15" letter-spacing="1.5" text-anchor="middle">DR MARISA HOLLEND</text>
  </g>

  <!-- Offer title -->
  <text class="intro" x="217" y="303">We are running a</text>
  <text class="offer-script" x="30" y="418">Special</text>
  <text class="offer-word" x="160" y="530">offer</text>
  <path class="title-swoosh" d="M62 606 C 200 560 330 548 416 566 C 330 558 210 574 62 606 Z" fill="var(--white)"/>
  <text class="treatment" x="285" y="622" text-anchor="middle">for (Ortho) Braces/Clear</text>
  <text class="treatment" x="285" y="652" text-anchor="middle">Aligner (Quorvelina)</text>

  <!-- Discount badge -->
  <g class="discount-badge">
    <circle cx="628" cy="652" r="166" fill="var(--white)" opacity="0.4"/>
    <circle cx="628" cy="652" r="146" fill="var(--white)"/>
    <text class="badge-lead" x="628" y="587" text-anchor="middle">Up to</text>
    <text class="badge-amount" x="628" y="638" text-anchor="middle">$2,000 off</text>
    <text class="badge-note" x="628" y="669" text-anchor="middle">with free Consultation</text>
    <text class="badge-note" x="628" y="691" text-anchor="middle">and Xrays</text>
    <line x1="606" y1="713" x2="650" y2="713" stroke="var(--purple)" stroke-width="3"/>
    <text class="badge-date" x="628" y="751" text-anchor="middle">Till <tspan class="dark">July 31st</tspan> 2020</text>
  </g>

  <!-- Headline -->
  <g class="mask-headline">
    <text class="headline" x="50" y="877">WHAT BETTER TIME TO</text>
    <text class="headline" x="50" y="918"><tspan class="dark">GET BRACES</tspan> WHEN YOU HAVE</text>
    <text class="headline" x="50" y="960">TO <tspan class="dark">WEAR A MASK</tspan> ALL THE TIME.</text>
  </g>

  <!-- Contact -->
  <g class="contact">
    <text class="cta" x="714" y="868">CALL US FOR <tspan class="strong">FREE CONSULTATION</tspan></text>
    <line x1="714" y1="880" x2="780" y2="880" stroke="var(--white)" stroke-width="2"/>

    <g class="icon-phone" transform="translate(736 916)">
      <circle r="20" fill="none" stroke="var(--white)" stroke-width="2"/>
      <path d="M-8 -9 C -10 -3 -6 6 2 10 L 6 6 L 2 2 L -1 4 C -4 1 -5 -1 -5 -4 L -2 -6 L -5 -11 Z" fill="var(--white)"/>
      <path d="M3 -9 A 8 8 0 0 1 9 -3 M4 -14 A 13 13 0 0 1 14 -4" fill="none" stroke="var(--white)" stroke-width="1.8"/>
    </g>
    <text class="phone" x="768" y="936">+1 555-214-0382</text>

    <g class="icon-mail" transform="translate(740 966)">
      <circle r="18" fill="none" stroke="var(--white)" stroke-width="2"/>
      <rect x="-10" y="-7" width="20" height="14" fill="none" stroke="var(--white)" stroke-width="1.8"/>
      <path d="M-10 -7 L 0 2 L 10 -7" fill="none" stroke="var(--white)" stroke-width="1.8"/>
    </g>
    <text class="email" x="768" y="976">marisahollenddds@mailbox.com</text>
  </g>
</svg>
</body>
</html>
```